Kitchen and custom cabinetry company looking for business card design

We make: * Custom Kitchens, contemporary and traditional kitchens, Vanities, Libraries, Custom Entry Doors, Custom Wine Cellars and Custom Design Furniture. Phone number 555-318-2746. Address: Maple Hollow NY. Email: BRAVOK@mailbox.example Portfolio at: BRAVOKcabinetry.example I would like moderns fonts and not heavy lines. double side but maybe will use clear plastic. I attached the logo.

```html
<!DOCTYPE html>
<html lang="en">
<head>
<meta charset="utf-8">
<title>BRAVOK Cabinetry Inc. – Business Card</title>
<link rel="stylesheet" href="https://fonts.googleapis.com/css2?family=Lato:wght@300;400&display=swap">
<style>
  :root {
    --stage: #1c1c1e;
    --card-dark: #141416;
    --card-mid: #2a2a2d;
    --name-grey: #9a9a9c;
    --accent: #f0602a;
    --text-light: #f2f2f2;
    --label-grey: #a8a8ab;
  }
  * { box-sizing: border-box; margin: 0; padding: 0; }
  html, body {
    width: 1200px; height: 900px; overflow: hidden;
    background: var(--stage);
    font-family: "Lato", "Helvetica Neue", Arial, sans-serif;
  }
  .canvas {
    width: 1200px; height: 900px;
    display: flex; align-items: center; justify-content: center; gap: 40px;
  }
  .card {
    width: 540px; height: 310px; border-radius: 14px;
    position: relative; overflow: hidden;
    background:
      linear-gradient(100deg, rgba(255,255,255,0.06), rgba(255,255,255,0) 40%, rgba(255,255,255,0.05) 70%, rgba(255,255,255,0) 100%),
      linear-gradient(180deg, var(--card-mid), var(--card-dark));
    box-shadow: 0 18px 40px rgba(0,0,0,0.55);
    color: var(--text-light);
    padding: 0 24px;
  }
  .card-surface { position: absolute; inset: 0; }
  .card-content {
    position: relative; height: 100%;
    display: flex; flex-direction: column; align-items: center; justify-content: center;
    text-align: center;
  }

  /* front */
  .brand { display: flex; align-items: center; gap: 12px; white-space: nowrap; }
  .brand-mark { width: 14px; height: 14px; background: var(--accent); flex: none; }
  .brand-name {
    font-weight: 300; font-size: 28px; letter-spacing: 3px;
    color: var(--name-grey); text-transform: uppercase; line-height: 1;
  }
  .tagline {
    margin-top: 12px; font-size: 11.5px; letter-spacing: 2.2px;
    color: var(--accent); text-transform: uppercase;
  }
  .services { margin-top: 30px; font-size: 13px; line-height: 1.55; font-weight: 300; }
  .services .sep { color: var(--accent); padding: 0 4px; }
  .front-web { margin-top: 4px; font-size: 11.5px; color: var(--accent); }

  /* back */
  .contact-item { display: flex; flex-direction: column; align-items: center; }
  .contact-label { font-size: 11px; color: var(--label-grey); font-weight: 300; line-height: 1.2; }
  .contact-value { font-size: 15px; line-height: 1.25; }
  .divider {
    display: block; width: 26px; height: 2px; margin: 9px 0 7px;
    background: var(--accent);
  }
</style>
</head>
<body>
<main class="canvas">
  <section class="card front" aria-label="Card front">
    <div class="card-surface" role="img" aria-label="Dark brushed metal finish"></div>
    <div class="card-content">
      <div class="brand">
        <span class="brand-mark" aria-hidden="true"></span>
        <span class="brand-name">BRAVOK Cabinetry Inc.</span>
      </div>
      <p class="tagline">Construction of Interior Solutions</p>
      <p class="services">
        Custom Kitchens<span class="sep">|</span>Contemporary and Traditional Kitchens<span class="sep">|</span>Vanities<br>
        Libraries<span class="sep">|</span>Custom Entry Doors<span class="sep">|</span>Custom Wine Cellars<span class="sep">|</span>Custom Design Furniture
      </p>
      <p class="front-web">www.BRAVOKcabinetry.example</p>
    </div>
  </section>

  <section class="card back" aria-label="Card back">
    <div class="card-surface" role="img" aria-label="Dark brushed metal finish"></div>
    <div class="card-content">
      <div class="contact-item">
        <span class="contact-label">phone:</span>
        <span class="contact-value">555-318-2746</span>
      </div>
      <span class="divider" aria-hidden="true"></span>
      <div class="contact-item">
        <span class="contact-label">address:</span>
        <span class="contact-value">Maple Hollow NY</span>
      </div>
      <span class="divider" aria-hidden="true"></span>
      <div class="contact-item">
        <span class="contact-label">email:</span>
        <span class="contact-value">BRAVOK@mailbox.example</span>
      </div>
      <span class="divider" aria-hidden="true"></span>
      <div class="contact-item">
        <span class="contact-label">portfolio:</span>
        <span class="contact-value">www.BRAVOKcabinetry.example</span>
      </div>
    </div>
  </section>
</main>
</body>
</html>
```